33.5 x 80 - Retractable Banner - Bluegate Lending Partners Inc.

Bluegate Lending Partners, Inc.

A Community Based Mortgage Broker
Offering a Full Line of Mortgage Loan Products

Home of the Mortgage Originating Real Estate Experts

"Open the Bluegate, we'll carry the weight"

Licensed in DC, MD and VA

EST 1997
NMLS #317846
Phone (800) 926-4051
www.bluegatehomeloans.com
www.workatbluegate.cocm
@youopenbluegate

```html
<!DOCTYPE html>
<html lang="en">
<head>
<meta charset="utf-8">
<title>Bluegate Lending Partners – Retractable Banner</title>
<link rel="stylesheet" href="https://fonts.googleapis.com/css2?family=Bebas+Neue&family=Montserrat:wght@500;700;800&display=swap">
<style>
  :root{
    --navy:#0b0c4a;
    --royal:#2b3d9c;
    --blue:#3a68c0;
    --banner-blue:#3447a4;
    --gold:#e2b24a;
    --gold-dark:#b8862b;
    --white:#ffffff;
    --ink:#111111;
    --bullet:#f5d020;
  }
  html,body{margin:0;padding:0;width:1200px;height:2533px;overflow:hidden;background:#fff;}
  .banner{display:block;width:1200px;height:2533px;}
  .display{font-family:"Bebas Neue",sans-serif;}
  .sans{font-family:"Montserrat",sans-serif;}
  .intro{fill:var(--white);font-size:68px;letter-spacing:1px;}
  .headline{fill:var(--gold);font-size:105px;font-weight:800;}
  .headline-shadow{fill:var(--navy);font-size:105px;font-weight:800;}
  .kicker{fill:var(--ink);font-size:76px;}
  .experts{font-size:146px;}
  .experts .dark{fill:var(--royal);}
  .experts .light{fill:var(--blue);}
  .brand-name{fill:var(--royal);font-size:34px;font-weight:800;}
  .brand-tag{fill:var(--royal);font-size:18px;font-weight:700;}
  .brand-est{fill:var(--gold-dark);font-size:20px;font-weight:700;letter-spacing:5px;}
  .quote{fill:var(--white);font-size:56px;font-weight:800;}
  .phone{fill:var(--white);font-size:115px;}
  .web{fill:var(--white);font-size:38px;font-weight:700;}
  .facts{fill:var(--white);font-size:34px;font-weight:500;}
  .bullet{fill:var(--bullet);}
</style>
</head>
<body>
<svg class="banner" viewBox="0 0 1200 2533" xmlns="http://www.w3.org/2000/svg">
  <defs>
    <linearGradient id="topGrad" x1="0" y1="0" x2="0" y2="1">
      <stop offset="0" stop-color="#0a0a45"/>
      <stop offset="0.3" stop-color="#2a3f9a"/>
      <stop offset="0.6" stop-color="#4a6ea8"/>
      <stop offset="1" stop-color="#8fa6c0"/>
    </linearGradient>
    <radialGradient id="heroWarm" cx="0.6" cy="0.62" r="0.45">
      <stop offset="0" stop-color="#e0cdb8" stop-opacity="0.75"/>
      <stop offset="0.55" stop-color="#a9a3a8" stop-opacity="0.35"/>
      <stop offset="1" stop-color="#4a6ea8" stop-opacity="0"/>
    </radialGradient>
    <radialGradient id="heroLight" cx="0.2" cy="0.82" r="0.3">
      <stop offset="0" stop-color="#dfe6ee" stop-opacity="0.8"/>
      <stop offset="1" stop-color="#dfe6ee" stop-opacity="0"/>
    </radialGradient>
    <linearGradient id="goldGrad" x1="0" y1="0" x2="1" y2="0">
      <stop offset="0" stop-color="#b8862b"/>
      <stop offset="0.5" stop-color="#f3d27a"/>
      <stop offset="1" stop-color="#c99a3a"/>
    </linearGradient>
    <linearGradient id="photoA" x1="0" y1="0" x2="1" y2="1">
      <stop offset="0" stop-color="#3c4c7e"/>
      <stop offset="1" stop-color="#1e2540"/>
    </linearGradient>
    <linearGradient id="photoB" x1="0" y1="0" x2="1" y2="1">
      <stop offset="0" stop-color="#c9ced6"/>
      <stop offset="1" stop-color="#4a4f5c"/>
    </linearGradient>
  </defs>

  <!-- Top hero -->
  <g role="img" aria-label="Photo: a delighted businesswoman in a beige blazer celebrating at her laptop in a bright office">
    <rect x="0" y="0" width="1200" height="1100" fill="url(#topGrad)"/>
    <rect x="0" y="0" width="1200" height="1100" fill="url(#heroWarm)"/>
    <rect x="0" y="0" width="1200" height="1100" fill="url(#heroLight)"/>
  </g>

  <text class="display intro" x="600" y="143" text-anchor="middle">A COMMUNITY BASED MORTGAGE BROKER</text>
  <line x1="150" y1="180" x2="305" y2="180" stroke="#fff" stroke-width="2"/>
  <line x1="895" y1="180" x2="1050" y2="180" stroke="#fff" stroke-width="2"/>
  <text class="display intro" x="600" y="205" text-anchor="middle">OFFERING A FULL LINE OF</text>

  <text class="sans headline-shadow" x="605" y="323" text-anchor="middle">MORTGAGE</text>
  <text class="sans headline" x="600" y="318" text-anchor="middle">MORTGAGE</text>
  <text class="sans headline-shadow" x="605" y="416" text-anchor="middle">LOAN PRODUCTS</text>
  <text class="sans headline" x="600" y="411" text-anchor="middle">LOAN PRODUCTS</text>

  <!-- Middle white section with gold swoosh -->
  <path d="M0 1078 C380 1120 820 1020 1200 870 L1200 1100 L0 1100 Z" fill="url(#goldGrad)"/>
  <path d="M0 1092 C380 1132 820 1040 1200 898 L1200 1700 L0 1700 Z" fill="var(--royal)"/>
  <path d="M0 1102 C380 1142 820 1052 1200 912 L1200 1700 L0 1700 Z" fill="var(--white)"/>

  <!-- Portrait circle 1 -->
  <circle cx="295" cy="1142" r="207" fill="var(--white)"/>
  <circle cx="295" cy="1142" r="198" fill="var(--royal)"/>
  <circle cx="295" cy="1142" r="184" fill="url(#photoA)" role="img" aria-label="Portrait of a company executive in a dark suit"/>

  <!-- Brand -->
  <circle cx="852" cy="1200" r="44" fill="none" stroke="var(--royal)" stroke-width="6"/>
  <text class="sans brand-name" x="852" y="1306" text-anchor="middle">BLUEGATE LENDING PARTNERS</text>
  <line x1="650" y1="1322" x2="1054" y2="1322" stroke="var(--royal)" stroke-width="2"/>
  <text class="sans brand-tag" x="852" y="1350" text-anchor="middle">OPEN THE BLUEGATE, WE'LL CARRY THE WEIGHT.</text>
  <text class="sans brand-est" x="852" y="1382" text-anchor="middle">EST. 1997</text>

  <text class="display kicker" x="600" y="1481" text-anchor="middle">HOME OF THE MORTGAGE ORIGINATING</text>
  <text class="display experts" x="600" y="1600" text-anchor="middle"><tspan class="dark">REAL </tspan><tspan class="light">ESTATE EXPERTS</tspan></text>

  <!-- Bottom blue section -->
  <path d="M0 1970 C300 1790 700 1680 1200 1640 L1200 1668 C700 1705 300 1815 0 2000 Z" fill="url(#goldGrad)"/>
  <path d="M0 2000 C300 1815 700 1705 1200 1668 L1200 2533 L0 2533 Z" fill="var(--banner-blue)"/>

  <!-- Portrait circle 2 -->
  <circle cx="340" cy="1884" r="266" fill="var(--white)"/>
  <circle cx="340" cy="1884" r="252" fill="var(--blue)"/>
  <circle cx="340" cy="1884" r="230" fill="url(#photoB)" role="img" aria-label="Photo: a loan officer on the phone at his office desk"/>

  <text class="sans quote" text-anchor="middle">
    <tspan x="909" y="1877">“OPEN THE</tspan>
    <tspan x="909" y="1941">BLUEGATE,</tspan>
    <tspan x="909" y="2005">WE’LL CARRY</tspan>
    <tspan x="909" y="2069">THE WEIGHT”</tspan>
  </text>

  <!-- Contact -->
  <g fill="var(--white)">
    <rect x="90" y="2212" width="52" height="82" rx="10"/>
    <rect x="99" y="2225" width="34" height="54" fill="var(--banner-blue)"/>
    <path d="M74 2228 q-14 22 0 46 l11 -6 q-9 -17 0 -34 z"/>
  </g>
  <text class="display phone" x="172" y="2290">(800) 926-4051</text>

  <circle cx="115" cy="2366" r="42" fill="var(--gold)"/>
  <g fill="none" stroke="var(--white)" stroke-width="3">
    <circle cx="115" cy="2366" r="23"/>
    <ellipse cx="115" cy="2366" rx="10" ry="23"/>
    <line x1="92" y1="2366" x2="138" y2="2366"/>
  </g>
  <text class="sans web" x="176" y="2352">www.bluegatehomeloans.com</text>
  <text class="sans web" x="176" y="2399">www.workatbluegate.com</text>
  <text class="sans web" x="176" y="2453">@youopenbluegate</text>

  <circle class="bullet" cx="845" cy="2232" r="5"/>
  <text class="sans facts" x="863" y="2243">Licensed in</text>
  <text class="sans facts" x="863" y="2282">DC, MD and VA</text>
  <circle class="bullet" cx="845" cy="2320" r="5"/>
  <text class="sans facts" x="863" y="2331">EST 1997</text>
  <circle class="bullet" cx="845" cy="2357" r="5"/>
  <text class="sans facts" x="863" y="2368">NMLS #317846</text>
</svg>
</body>
</html>
```